Business Card Design Project

We need a business card design for an existing company in Dallas/Fort Worth that is expanding services and re-branding. We are changing the name from Brightmoor Commercial Cleaning to Keystride Facility Services. We are expanding from only commercial cleaning to include complete commercial landscape and facility maintenance services, too.

As stated, we offer a package of services that includes landscape, janitorial and facility services, which is largely unique in the industry.

We would like a design that communicates trust/partnership with a professional, corporate image, but not necessarily using the standard white business card. We would like a design that perhaps uses darker blues or perhaps a gray background, but we are open to other ideas. We might also be interested in a double-sided design - maybe with our logo on the back, printed on a gray background?

We will probably stick with the attached logo, but if you've got another inspired idea....

Target Market(s)

Property managers, commercial real estate professionals, corporate executives

Industry/Entity Type

Landscape

Requirements
Should not have
• Not interested in old style fonts.

```html
<!DOCTYPE html>
<html lang="en">
<head>
<meta charset="utf-8">
<title>Keystride Facility Services – Business Card</title>
<link href="https://fonts.googleapis.com/css2?family=Didact+Gothic&family=Roboto+Condensed:wght@400&family=Arimo:wght@700&display=swap" rel="stylesheet">
<style>
  :root {
    --panel-light: #6e6c6a;
    --panel-mid: #585553;
    --panel-dark: #353230;
    --ink-light: #ffffff;
    --divider: #9a9896;
    --frame: #8d8b89;
  }
  * { margin: 0; padding: 0; box-sizing: border-box; }
  html, body {
    width: 960px; height: 1200px; overflow: hidden;
    background: #ffffff;
  }
  .card-sheet {
    position: relative;
    width: 960px; height: 1200px;
    border: 1px solid var(--frame);
    overflow: hidden;
  }
  .card-face {
    position: absolute; left: 0; width: 100%;
    background: radial-gradient(ellipse 90% 110% at 8% 55%, var(--panel-light) 0%, var(--panel-mid) 45%, var(--panel-dark) 100%);
  }
  .card-front { top: 0; height: 600px; }
  .card-back { top: 600px; height: 600px; border-top: 1px solid var(--divider); }

  .brand-mark {
    position: absolute; left: 491px; top: 114px;
    width: 124px; height: 110px;
  }
  .brand-name {
    position: absolute; left: 0; right: 0; top: 262px;
    text-align: center;
    font-family: "Didact Gothic", sans-serif;
    font-size: 56px; letter-spacing: 1px;
    color: var(--ink-light);
  }
  .tagline {
    position: absolute; left: 0; right: 0; top: 412px;
    text-align: center;
    font-family: "Didact Gothic", sans-serif;
    font-size: 35px; line-height: 52px;
    color: var(--ink-light);
  }

  .contact-name {
    position: absolute; left: 82px; top: 194px;
    font-family: "Arimo", sans-serif; font-weight: 700;
    font-size: 31px; color: var(--ink-light);
  }
  .contact-title {
    position: absolute; left: 82px; top: 236px;
    font-family: "Roboto Condensed", sans-serif;
    font-size: 30px; color: var(--ink-light);
  }
  .contact-mobile {
    position: absolute; left: 583px; top: 248px;
    font-family: "Roboto Condensed", sans-serif;
    font-size: 28px; color: var(--ink-light);
  }
  .contact-list {
    position: absolute; left: 76px; top: 403px;
    font-family: "Roboto Condensed", sans-serif;
    font-size: 28px; line-height: 32px; color: var(--ink-light);
    list-style: none;
  }
  .contact-list li { display: flex; }
  .contact-label { width: 139px; }
</style>
</head>
<body>
  <main class="card-sheet">
    <section class="card-face card-front">
      <svg class="brand-mark" viewBox="0 0 124 110" aria-hidden="true">
        <rect x="3.5" y="3.5" width="117" height="103" fill="none" stroke="#ffffff" stroke-width="7"/>
      </svg>
      <h1 class="brand-name">Keystride Facility Services</h1>
      <p class="tagline">One source for Landscape, Janitorial<br>and Facility Maintenance</p>
    </section>

    <section class="card-face card-back">
      <h2 class="contact-name">Grant Whitaker</h2>
      <p class="contact-title">General Manager</p>
      <p class="contact-mobile">Mobile&nbsp; :</p>
      <ul class="contact-list">
        <li><span class="contact-label">Address</span><span>:</span></li>
        <li><span class="contact-label">Phone</span><span>:</span></li>
        <li><span class="contact-label">Fax</span><span>:</span></li>
        <li><span class="contact-label">Email</span><span>:</span></li>
      </ul>
    </section>
  </main>
</body>
</html>
```